redesing professional certificate

Redesign our certificate to more a professional look and to make it look like a-wanna have - Best in adobe photoshop, because this template will be our basic, and we have in our education different levels, basic, upper, lower, complex, master level. I usually add a small picture to show what level they are. Or when you have a better suggestion I a gladly to hear.
We teach to physiotherapist so it has to look professional.

Target Market(s)

physiotherapist

Industry/Entity Type

Health Care

Requirements
Must have
• our logo

```html
<!DOCTYPE html>
<html lang="en">
<head>
<meta charset="utf-8">
<title>Certificate – Meridian Fascia Method</title>
<link href="https://fonts.googleapis.com/css2?family=Playfair+Display:wght@800;900&family=Montserrat:ital,wght@0,600;1,400;1,500&display=swap" rel="stylesheet">
<style>
  :root {
    --navy: #13233f;
    --yellow: #f9c91f;
    --grey: #b3b3b3;
    --paper: #ffffff;
    --wash: #f2f2f2;
    --wash-text: #e6e6e6;
  }
  * { margin: 0; padding: 0; box-sizing: border-box; }
  html, body { width: 849px; height: 1200px; overflow: hidden; background: var(--paper); }
  .certificate {
    position: relative; width: 849px; height: 1200px; overflow: hidden;
    background: var(--paper); color: var(--navy);
    font-family: "Montserrat", Arial, sans-serif;
    border: 1px solid #e4e4e4;
  }
  .stripe { position: absolute; top: 0; bottom: 0; }
  .stripe--navy { left: 0; width: 29px; background: var(--navy); }
  .stripe--yellow { left: 39px; width: 14px; background: var(--yellow); }

  .backdrop-disc {
    position: absolute; left: 160px; top: 550px; width: 760px; height: 760px;
    border-radius: 50%; background: var(--wash);
  }
  .backdrop-name {
    position: absolute; left: 230px; top: 1150px; width: 620px;
    font-family: "Montserrat", Arial, sans-serif; font-weight: 600;
    font-size: 34px; color: var(--wash-text); white-space: nowrap; letter-spacing: 0.5px;
  }

  .brand {
    position: absolute; top: 62px; left: 0; right: 0;
    display: flex; align-items: center; justify-content: center; gap: 12px;
  }
  .brand__dot { width: 22px; height: 22px; border-radius: 50%; background: var(--yellow); }
  .brand__name {
    font-family: "Montserrat", Arial, sans-serif; font-weight: 600;
    font-size: 22px; letter-spacing: 2px; color: var(--navy); text-transform: uppercase;
  }

  .title {
    position: absolute; left: 107px; top: 190px;
    font-family: "Playfair Display", Georgia, serif; font-weight: 900;
    font-size: 92px; line-height: 1; letter-spacing: 1px; color: var(--navy);
  }
  .recipient {
    position: absolute; left: 107px; top: 358px;
    font-family: "Playfair Display", Georgia, serif; font-weight: 800;
    font-size: 29px; letter-spacing: 0.3px; text-transform: uppercase;
  }
  .italic { font-style: italic; font-weight: 400; font-size: 22px; line-height: 31.5px; }
  .course { position: absolute; left: 107px; top: 409px; }

  .signature { position: absolute; top: 578px; font-size: 22px; line-height: 29px; font-style: italic; font-weight: 400; }
  .signature--left { left: 107px; }
  .signature--right { right: 117px; text-align: center; }
  .signature--left .signature__role { padding-left: 33px; }

  .registration { position: absolute; left: 107px; top: 703px; }
  .terms { position: absolute; left: 107px; top: 766px; width: 680px; }
  .address { position: absolute; left: 108px; top: 912px; }
  .tagline { position: absolute; left: 108px; top: 1069px; }

  .dot { position: absolute; width: 50px; height: 50px; border-radius: 50%; }
  .dot--yellow { left: 678px; top: 930px; background: var(--yellow); }
  .dot--grey { left: 643px; top: 992px; background: var(--grey); }
  .dot--navy { left: 714px; top: 992px; background: var(--navy); }
</style>
</head>
<body>
<main class="certificate">
  <div class="stripe stripe--navy"></div>
  <div class="stripe stripe--yellow"></div>

  <div class="backdrop-disc"></div>
  <div class="backdrop-name">MERIDIAN FASCIA METHOD</div>

  <header class="brand">
    <span class="brand__dot"></span>
    <span class="brand__name">Meridian Fascia Method</span>
  </header>

  <h1 class="title">CERTIFICATE</h1>

  <p class="recipient">Tomas Alvarenga</p>

  <p class="course italic">
    has completed the fasciatherapy level I course<br>
    - 3 days, 75-77 february 2020 -<br>
    Kópavogur, Iceland 77 february 2020.
  </p>

  <div class="signature signature--left">
    <div class="signature__name">Mr. JH v.d. Berg</div>
    <div class="signature__role">Co-Director</div>
  </div>
  <div class="signature signature--right">
    <div class="signature__name">Mr. RM Hadley</div>
    <div class="signature__role">Co-Director</div>
  </div>

  <p class="registration italic">Registration number: 7 ICE 20</p>

  <p class="terms italic">
    The Meridian Fascia Method ongoing certification is contingent upon meeting the requirements of the maintenance of the certification of Fasciatherapy.
  </p>

  <address class="address italic">
    Tissuelink BV<br>
    Noorderhavenkade 14<br>
    1013AB Amsterdam<br>
    The Netherlands
  </address>

  <p class="tagline italic">Specialists in fasciatherapy innovation</p>

  <span class="dot dot--yellow"></span>
  <span class="dot dot--grey"></span>
  <span class="dot dot--navy"></span>
</main>
</body>
</html>
```